" Temos como objetivo melhor atender as demandas atuais em TI com suporte de fácil acesso e analistas especializados com certificações que o mercado atual exige. Nossa equipe se dedica à prevenção, resolução de problemas e sugestões de melhorias do ambiente para garantir que seus servidores e aplicações estejam sempre no ar e funcionando, garantindo a continuidade dos negócios, foco das nossas soluções. "

```html
<!DOCTYPE html>
<html lang="pt-BR">
<head>
<meta charset="UTF-8">
<title>Nordavi – Envelopes</title>
<link href="https://fonts.googleapis.com/css2?family=Montserrat:wght@300;400;500&display=swap" rel="stylesheet">
<style>
  :root {
    --bg: #d4d5d7;
    --paper: #ffffff;
    --navy: #0f2a47;
    --ink: #1c2f4a;
    --orange: #f39a1e;
    --orange-deep: #f0622a;
    --yellow: #f8c21a;
    --muted: #4a4f57;
  }
  * { margin: 0; padding: 0; box-sizing: border-box; }
  html, body { width: 1200px; height: 1200px; overflow: hidden; }
  body {
    background: var(--bg);
    font-family: "Montserrat", sans-serif;
    position: relative;
  }
  .envelope {
    position: absolute;
    top: 276px;
    height: 652px;
    width: 436px;
  }
  .envelope--front { left: 156px; background: var(--paper); }
  .envelope--back { left: 612px; background: var(--navy); }

  .envelope__flap {
    position: absolute;
    top: 0; left: 0;
    width: 100%;
    height: 58px;
    background: linear-gradient(90deg, var(--orange-deep) 0%, var(--orange) 50%, var(--yellow) 100%);
    clip-path: polygon(0 0, 100% 0, 97% 100%, 3% 100%);
  }

  .brand {
    position: absolute;
    top: 360px;
    left: 0; right: 0;
    display: flex;
    align-items: center;
    justify-content: center;
    gap: 14px;
  }
  .envelope--back .brand { top: 344px; }
  .brand__dot {
    width: 30px; height: 30px;
    border-radius: 50%;
    background: var(--orange);
  }
  .brand__name {
    font-weight: 400;
    font-size: 44px;
    letter-spacing: 10px;
    color: var(--ink);
    line-height: 1;
  }
  .envelope--back .brand__name { color: #ffffff; }

  .contact {
    position: absolute;
    bottom: 40px;
    left: 40px; right: 30px;
    display: flex;
    justify-content: space-between;
    align-items: center;
  }
  .contact__item {
    display: flex;
    align-items: center;
    gap: 7px;
    font-size: 10px;
    color: var(--muted);
    font-weight: 500;
  }
  .contact__icon {
    width: 16px; height: 16px;
    border-radius: 3px;
    background: var(--orange);
    display: flex; align-items: center; justify-content: center;
  }
  .contact__icon svg { width: 10px; height: 10px; }
</style>
</head>
<body>
  <section class="envelope envelope--front">
    <div class="envelope__flap"></div>
    <div class="brand">
      <span class="brand__dot"></span>
      <span class="brand__name">NORDAVI</span>
    </div>
    <footer class="contact">
      <div class="contact__item">
        <span class="contact__icon">
          <svg viewBox="0 0 10 10"><path d="M2 1h2l1 2-1 1a5 5 0 0 0 2 2l1-1 2 1v2a1 1 0 0 1-1 1A8 8 0 0 1 1 2a1 1 0 0 1 1-1z" fill="#fff"/></svg>
        </span>
        43 90000-4127
      </div>
      <div class="contact__item">
        <span class="contact__icon">
          <svg viewBox="0 0 10 10"><circle cx="5" cy="5" r="3.8" fill="none" stroke="#fff" stroke-width="1"/><path d="M1.2 5h7.6M5 1.2c-2 2.5-2 5.1 0 7.6M5 1.2c2 2.5 2 5.1 0 7.6" fill="none" stroke="#fff" stroke-width="0.8"/></svg>
        </span>
        nordavi.com.br
      </div>
      <div class="contact__item">
        <span class="contact__icon">
          <svg viewBox="0 0 10 10"><rect x="1" y="2.2" width="8" height="5.6" fill="none" stroke="#fff" stroke-width="1"/><path d="M1 2.5l4 3 4-3" fill="none" stroke="#fff" stroke-width="1"/></svg>
        </span>
        contato@nordavi.com.br
      </div>
    </footer>
  </section>

  <section class="envelope envelope--back">
    <div class="brand">
      <span class="brand__dot"></span>
      <span class="brand__name">NORDAVI</span>
    </div>
  </section>
</body>
</html>
```